Brightwell Systems, a software development company, needs a website

We need a website to promote our software development company. The company is brand new and we want to market ourselves. We develop all kinds of software from web applications, to desktop applications, to mobile applications. Small company, not a lot of history, just need something flashy.

```html
<!DOCTYPE html>
<html lang="en">
<head>
<meta charset="utf-8">
<title>Brightwell Systems Inc</title>
<link href="https://fonts.googleapis.com/css2?family=Rajdhani:wght@400;500;600&family=Lato:wght@400;700&family=Poppins:wght@600;700&display=swap" rel="stylesheet">
<style>
:root{
  --navy:#065a85;
  --sky:#1795cf;
  --ink:#4a4a4a;
  --text:#6b6b6b;
  --line:#d5d5d5;
  --black:#111;
}
*{box-sizing:border-box;margin:0;padding:0}
html,body{width:706px;height:1200px;overflow:hidden;background:#fff}
body{position:relative;font-family:'Lato',sans-serif;color:var(--text)}
.abs{position:absolute}

.nav-strip{left:0;top:0;width:706px;height:20px;background:var(--sky)}
.nav{right:96px;top:0;height:20px;display:flex;gap:16px;align-items:center;font-family:'Poppins',sans-serif;font-weight:600;font-size:6px;color:#fff}
.brand-panel{left:0;top:0}
.brand{left:96px;top:12px;font-family:'Poppins',sans-serif;font-weight:700;font-size:13px;color:#fff}

.hero{left:0;top:26px;width:706px;height:331px}
.hero-base{left:0;top:357px;width:706px;height:11px;background:var(--navy)}
.hero-title{left:101px;font-family:'Rajdhani',sans-serif;font-weight:500;font-size:40px;line-height:1;color:#fff;letter-spacing:1px}
.hero-title.l1{top:86px}
.hero-title.l2{top:130px;left:95px;width:184px;height:41px;background:var(--sky);padding:3px 0 0 6px;color:var(--black)}
.hero-title.l3{top:178px}
.bar{width:35px;height:4px;background:var(--sky);left:99px}
.tagline{left:100px;top:247px;font-family:'Rajdhani',sans-serif;font-weight:500;font-size:13px;line-height:16px;color:#e8e8e8;letter-spacing:.3px}

.section-title{font-family:'Rajdhani',sans-serif;font-weight:500;font-size:29px;line-height:1;color:var(--ink);letter-spacing:.5px}
.section-title span{color:var(--navy);font-weight:600}
.copy{font-size:7px;line-height:11.4px;color:var(--text)}
.btn{background:var(--sky);color:#fff;font-family:'Rajdhani',sans-serif;font-weight:500;font-size:8px;display:flex;align-items:center;justify-content:center}

.card{left:360px;width:251px;height:92px;border:1px solid var(--line);border-radius:2px;padding:11px 9px}
.card h3{font-family:'Lato',sans-serif;font-weight:700;font-size:8.5px;color:#111}
.card .date{font-size:6px;color:var(--sky);margin:3px 0 4px}

.service{left:95px;width:260px;height:50px}
.service .icon{position:absolute;left:0;top:0;width:40px;height:40px;background:var(--navy);border-radius:2px;display:flex;align-items:center;justify-content:center}
.service .icon.outline{background:#fff;border:1px solid var(--navy)}
.service h4{position:absolute;left:56px;top:-1px;font-family:'Rajdhani',sans-serif;font-weight:500;font-size:11.5px;color:#222}
.service p{position:absolute;left:56px;top:15px;width:200px}

.touch{left:360px;top:693px;width:346px;height:132px;background:var(--navy)}
.touch-icon{left:368px;top:676px;width:40px;height:37px;background:var(--navy);border:3px solid #fff;display:flex;align-items:center;justify-content:center}
.touch h3{left:416px;top:700px;font-family:'Rajdhani',sans-serif;font-weight:500;font-size:15.5px;line-height:18px;color:#fff}
.touch-copy{left:416px;top:739px;width:190px;color:#fff}
.phone-btn{left:415px;top:788px;width:106px;height:24px;background:#fff;color:var(--navy);font-family:'Rajdhani',sans-serif;font-weight:600;font-size:13px;display:flex;align-items:center;justify-content:center}

.field{border:1px solid var(--line);border-radius:2px;font-size:6.5px;color:#777;padding:0 7px;display:flex;align-items:center}
.field.msg{align-items:flex-start;padding-top:6px}

.footer{left:0;top:1086px;width:706px;height:88px;background:var(--navy)}
.footer-item{top:1118px;display:flex;align-items:center;gap:10px;color:#fff;font-size:7px;line-height:11.4px}
.ring{width:22px;height:22px;border:1.5px solid #fff;border-radius:50%;display:flex;align-items:center;justify-content:center;flex:none}
.footer-brand{left:540px;top:1100px;width:140px;text-align:center;font-family:'Poppins',sans-serif;font-weight:700;font-size:15.5px;line-height:20px;color:#fff}
.legal{left:0;top:1173px;width:706px;height:27px;background:#000;color:#fff;font-size:7px;display:flex;align-items:center;justify-content:center}
.legal b{font-weight:700}
</style>
</head>
<body>

<!-- Hero imagery -->
<svg class="abs hero" viewBox="0 0 706 331" role="img" aria-label="Photo of a software developer checking his phone beside a window, with a team working at laptops behind">
  <defs>
    <linearGradient id="heroDark" x1="0" y1="0" x2="1" y2="1">
      <stop offset="0" stop-color="#2a2d30"/>
      <stop offset=".6" stop-color="#1c1f22"/>
      <stop offset="1" stop-color="#2f3236"/>
    </linearGradient>
    <linearGradient id="heroLight" x1="0" y1="0" x2="1" y2="0">
      <stop offset="0" stop-color="#5b6470"/>
      <stop offset=".5" stop-color="#8a929c"/>
      <stop offset="1" stop-color="#d9dde0"/>
    </linearGradient>
  </defs>
  <rect width="706" height="331" fill="url(#heroDark)"/>
  <polygon points="377,0 706,0 706,331 377,331 427,167" fill="url(#heroLight)"/>
  <polygon points="362,0 377,0 427,167 377,331 362,331 441,167" fill="var(--sky)"/>
</svg>
<div class="abs hero-base"></div>

<!-- Header -->
<div class="abs nav-strip"></div>
<svg class="abs brand-panel" width="266" height="53" viewBox="0 0 266 53">
  <polygon points="0,0 264,0 243,45 0,45" fill="var(--navy)"/>
  <polygon points="0,44 244,44 264,0 266,0 245,53 0,53" fill="var(--sky)"/>
</svg>
<div class="abs brand">Brightwell Systems Inc</div>
<nav class="abs nav"><span>Home</span><span>About Us</span><span>Services</span><span>Blog</span><span>Contact Us</span></nav>

<div class="abs hero-title l1">WE GIVE</div>
<div class="abs hero-title l2">YOU BEST</div>
<div class="abs hero-title l3">SOFTWARE IDEA</div>
<div class="abs bar" style="top:241px"></div>
<div class="abs tagline">A SATISFIED CUSTOMER IS THE<br>BEST BUSINESS STRATEGY OF ALL.</div>
<div class="abs bar" style="top:281px"></div>

<!-- About -->
<h2 class="abs section-title" style="left:96px;top:399px">ABOUT <span>US</span></h2>
<p class="abs copy" style="left:96px;top:442px;width:252px">Lorem Ipsum is simply dummy text of the printing and typesetting industry. Lorem Ipsum has been the industry's standard dummy text ever since the 1500s, when an unknown printer took a galley of type and scrambled it to make a type specimen book. It has survived not only five centuries, but also the leap into electronic typesetting, remaining essentially unchanged.</p>
<div class="abs btn" style="left:95px;top:523px;width:70px;height:22px">Get Started Now</div>

<!-- Blog -->
<h2 class="abs section-title" style="left:361px;top:399px">LATEST <span>BLOG</span></h2>
<article class="abs card" style="top:446px">
  <h3>Lorem Ipsum is simply dummy text.</h3>
  <div class="date">2-Aug-2019</div>
  <p class="copy">Lorem Ipsum is simply dummy text of the printing and typesetting industry. Lorem Ipsum has been the industry's standard dummy text ever since the 1500s, when an unknown printer took a galley of type and scrambled it to make a type specimen book.</p>
</article>
<article class="abs card" style="top:552px">
  <h3>Lorem Ipsum is simply dummy text.</h3>
  <div class="date">2-Aug-2019</div>
  <p class="copy">Lorem Ipsum is simply dummy text of the printing and typesetting industry. Lorem Ipsum has been the industry's standard dummy text ever since the 1500s, when an unknown printer took a galley of type and scrambled it to make a type specimen book.</p>
</article>

<!-- Services -->
<h2 class="abs section-title" style="left:96px;top:584px">OUR <span>SERVICES</span></h2>
<div class="abs service" style="top:635px">
  <div class="icon"><svg width="18" height="26" viewBox="0 0 18 26" fill="none" stroke="#fff" stroke-width="1.5"><rect x="2" y="1" width="14" height="24" rx="2"/><line x1="2" y1="5" x2="16" y2="5"/><line x1="2" y1="19" x2="16" y2="19"/><line x1="5" y1="9" x2="13" y2="9"/><line x1="5" y1="12" x2="10" y2="12"/><circle cx="9" cy="22" r=".8" fill="#fff"/></svg></div>
  <h4>Mobile Applications</h4>
  <p class="copy">Lorem Ipsum is simply dummy text of the printing and typesetting industry. Lorem Ipsum has been the industry's standard dummy text ever since the 1500s.</p>
</div>
<div class="abs service" style="top:701px">
  <div class="icon outline"><svg width="26" height="22" viewBox="0 0 26 22" fill="none" stroke="var(--navy)" stroke-width="1.5"><rect x="4" y="1" width="18" height="14"/><rect x="7" y="4" width="12" height="8"/><line x1="9" y1="7" x2="16" y2="7"/><line x1="9" y1="9.5" x2="14" y2="9.5"/><path d="M1 17h24v2a2 2 0 0 1-2 2H3a2 2 0 0 1-2-2z"/></svg></div>
  <h4>Web Applications</h4>
  <p class="copy">Lorem Ipsum is simply dummy text of the printing and typesetting industry. Lorem Ipsum has been the industry's standard dummy text ever since the 1500s.</p>
</div>
<div class="abs service" style="top:772px">
  <div class="icon"><svg width="24" height="22" viewBox="0 0 24 22" fill="none" stroke="#fff" stroke-width="1.5"><rect x="1" y="1" width="22" height="15" rx="1"/><line x1="5" y1="5" x2="16" y2="5"/><line x1="5" y1="8" x2="14" y2="8"/><line x1="5" y1="11" x2="12" y2="11"/><line x1="12" y1="16" x2="12" y2="20"/><line x1="7" y1="21" x2="17" y2="21"/></svg></div>
  <h4>Desktop Applications</h4>
  <p class="copy">Lorem Ipsum is simply dummy text of the printing and typesetting industry. Lorem Ipsum has been the industry's standard dummy text ever since the 1500s.</p>
</div>

<!-- Stay in touch -->
<div class="abs touch"></div>
<div class="abs touch-icon"><svg width="26" height="24" viewBox="0 0 26 24" fill="none" stroke="#fff" stroke-width="1.6" stroke-linecap="round"><path d="M5 3l4 0 2 5-2.5 1.5a11 11 0 0 0 6 6L16 13l5 2v4a2 2 0 0 1-2 2C10 21 3 14 3 5a2 2 0 0 1 2-2z" fill="#fff"/><path d="M15 8a3 3 0 0 1 3 3"/><path d="M15 4a7 7 0 0 1 7 7"/><path d="M15 0.5a10.5 10.5 0 0 1 10.5 10.5"/></svg></div>
<h3 class="abs" style="left:416px;top:700px;font-family:'Rajdhani',sans-serif;font-weight:500;font-size:15.5px;line-height:18px;color:#fff">Stay In Touch With Brightwell<br>Systems Inc.</h3>
<p class="abs copy touch-copy">Lorem Ipsum is simply dummy text of the printing and typesetting industry. Lorem Ipsum has been the industry's standard dummy text ever since the 1500s.</p>
<div class="abs phone-btn">+91-000-000-0000</div>

<!-- Contact -->
<h2 class="abs section-title" style="left:0;width:706px;text-align:center;top:869px">CONTACT <span>US</span></h2>
<div class="abs field" style="left:95px;top:916px;width:165px;height:24px">Name:</div>
<div class="abs field" style="left:270px;top:916px;width:165px;height:24px">Email:</div>
<div class="abs field" style="left:446px;top:916px;width:165px;height:24px">Phone:</div>
<div class="abs field msg" style="left:95px;top:951px;width:516px;height:53px">Message:</div>
<div class="abs btn" style="left:322px;top:1028px;width:62px;height:22px">Send message</div>

<!-- Footer -->
<div class="abs footer"></div>
<svg class="abs" style="left:0;top:1063px" width="706" height="111" viewBox="0 0 706 111">
  <polygon points="504,0 706,0 706,110 547,110 512,23 496,23" fill="var(--sky)"/>
</svg>
<div class="abs footer-item" style="left:95px">
  <div class="ring"><svg width="12" height="12" viewBox="0 0 26 24" fill="#fff"><path d="M5 3l4 0 2 5-2.5 1.5a11 11 0 0 0 6 6L16 13l5 2v4a2 2 0 0 1-2 2C10 21 3 14 3 5a2 2 0 0 1 2-2z"/></svg></div>
  <span>+91-000-000-0000</span>
</div>
<div class="abs footer-item" style="left:227px">
  <div class="ring"><svg width="12" height="9" viewBox="0 0 12 9" fill="none" stroke="#fff" stroke-width="1.2"><rect x=".6" y=".6" width="10.8" height="7.8"/><path d="M.6.6 6 5l5.4-4.4"/></svg></div>
  <span>support@brightwellsystems.<br>com</span>
</div>
<div class="abs footer-item" style="left:383px">
  <div class="ring"><svg width="9" height="12" viewBox="0 0 9 12" fill="#fff"><path d="M4.5 0A4.5 4.5 0 0 0 0 4.5C0 8 4.5 12 4.5 12S9 8 9 4.5A4.5 4.5 0 0 0 4.5 0zm0 6.3a1.8 1.8 0 1 1 0-3.6 1.8 1.8 0 0 1 0 3.6z"/></svg></div>
  <span>100 - Lorem ipsum is simply<br>dummy text.</span>
</div>
<div class="abs footer-brand">Brightwell<br>Systems Inc</div>
<div class="abs legal">Copyright © 2019&nbsp;<b>Brightwell Systems Inc.</b>&nbsp;All RightsReserved. Terms &amp; Conditions | Privacy Policy.</div>

</body>
</html>
```